Home Design company focused on remodel and enhancement of kitchens and bathroorms

I already have a logo designed by ArtHarbor, I now need a design for my business cards.
The company is in the remodeling and enhancement industry for homes, focusing on kitchens and bathrooms, however, we can remodel or enhance every room in a home, an office space, etc.

The company's name is VELMOR HOME DESIGN, LLC

We'll focus on clients in the Rio Grande Valley, Texas. Primarily McAllen, Edinburg, Pharr, Mission, Brownsville and South Padre Island.

The design on the business card should transmit reliability, professionalism anda bit of upscale design.

The logo is in black and white, and would like to keep it that way.

The information that needs to be printed in the business cards is:
Company's name: Velmor Home Design
Company's Logo (attached)
My name: Noel Bramwit
Address, phone and email:
2715 N Parkline Road, Ste 348
McAllen, TX 78501
(956) 555 0187
nbramwit@velmordesign.example
Website: velmordesign.example

```html
<!DOCTYPE html>
<html lang="en">
<head>
<meta charset="utf-8">
<title>Velmor Home Design – Business Card</title>
<link rel="stylesheet" href="https://fonts.googleapis.com/css2?family=Arimo:wght@400;700&family=Montserrat:wght@400&display=swap">
<style>
  :root {
    --backdrop: #e0e0e0;
    --paper: #ffffff;
    --ink: #1e1e1e;
    --ink-soft: #2a2a2a;
    --muted: #7d7d7d;
    --band-grey: #8a8a8a;
    --reverse: #ffffff;
  }
  * { box-sizing: border-box; margin: 0; padding: 0; }
  html, body { width: 1200px; height: 1200px; overflow: hidden; }
  body { background: var(--backdrop); position: relative; font-family: "Arimo", Arial, sans-serif; }

  .card {
    position: absolute;
    left: 163px;
    width: 874px;
    height: 498px;
    box-shadow: 2px 3px 5px rgba(0,0,0,0.3);
  }
  .card--front { top: 78px; background: var(--paper); }
  .card--back { top: 624px; background: var(--ink-soft); }

  .brand {
    position: absolute;
    display: flex;
    align-items: center;
    font-family: "Montserrat", Arial, sans-serif;
    font-weight: 400;
  }
  .brand__square { display: block; }
  .brand__rule { display: block; width: 2px; }
  .brand__name { text-transform: uppercase; line-height: 1.08; }
  .brand__name span { display: block; }

  .card--front .brand { left: 74px; top: 212px; color: var(--ink); }
  .card--front .brand__square { width: 70px; height: 70px; background: var(--ink); margin-right: 30px; }
  .card--front .brand__rule { height: 74px; background: var(--ink); margin-right: 16px; }
  .card--front .brand__name { font-size: 24px; letter-spacing: 5px; }

  .divider { position: absolute; left: 436px; top: 180px; width: 2px; height: 137px; background: var(--ink); }

  .person { position: absolute; left: 464px; top: 179px; }
  .person__name { font-weight: 700; font-size: 29px; color: var(--ink); letter-spacing: 0.2px; }
  .contact-list { list-style: none; margin-top: 22px; }
  .contact-list li { display: flex; align-items: center; font-size: 23px; color: var(--muted); height: 29px; }
  .contact-list svg { width: 18px; height: 18px; margin-right: 14px; flex: none; }

  .address-band { position: absolute; left: 0; top: 438px; width: 874px; height: 32px; }
  .address-band__dark {
    position: absolute; left: 0; top: 0; width: 731px; height: 32px; background: var(--ink);
    color: var(--reverse); font-size: 19px; line-height: 32px; text-align: right; padding-right: 48px;
  }
  .address-band__mark {
    position: absolute; left: 731px; top: 0; width: 96px; height: 32px;
    font-family: "Montserrat", Arial, sans-serif; font-size: 14px; letter-spacing: 2px;
    color: var(--ink); line-height: 32px; text-align: center;
  }
  .address-band__grey { position: absolute; left: 827px; top: 0; width: 47px; height: 32px; background: var(--band-grey); }

  .card--back .brand { left: 50%; top: 50%; transform: translate(-50%, -50%); color: var(--reverse); }
  .card--back .brand__square { width: 86px; height: 86px; background: var(--reverse); margin-right: 36px; }
  .card--back .brand__rule { height: 88px; background: var(--reverse); margin-right: 20px; }
  .card--back .brand__name { font-size: 30px; letter-spacing: 6px; }
</style>
</head>
<body>
  <section class="card card--front">
    <div class="brand">
      <span class="brand__square"></span>
      <span class="brand__rule"></span>
      <p class="brand__name"><span>Velmor</span><span>Home</span><span>Design</span></p>
    </div>

    <div class="divider"></div>

    <div class="person">
      <h1 class="person__name">NOEL BRAMWIT</h1>
      <ul class="contact-list">
        <li>
          <svg viewBox="0 0 24 24" aria-hidden="true"><path fill="#1e1e1e" d="M6.6 10.8c1.4 2.8 3.8 5.1 6.6 6.6l2.2-2.2c.3-.3.7-.4 1-.2 1.1.4 2.3.6 3.6.6.6 0 1 .4 1 1V20c0 .6-.4 1-1 1C10.6 21 3 13.4 3 4c0-.6.4-1 1-1h3.5c.6 0 1 .4 1 1 0 1.3.2 2.5.6 3.6.1.3 0 .7-.2 1L6.6 10.8z"/></svg>
          956-555 0187
        </li>
        <li>
          <svg viewBox="0 0 24 24" aria-hidden="true"><rect x="2.5" y="5" width="19" height="14" rx="2" fill="none" stroke="#1e1e1e" stroke-width="2"/><path d="M3 6l9 7 9-7" fill="none" stroke="#1e1e1e" stroke-width="2"/></svg>
          nbramwit@velmordesign.example
        </li>
        <li>
          <svg viewBox="0 0 24 24" aria-hidden="true"><g fill="none" stroke="#1e1e1e" stroke-width="1.8"><circle cx="12" cy="12" r="9.5"/><ellipse cx="12" cy="12" rx="4" ry="9.5"/><path d="M2.5 12h19M4 7h16M4 17h16"/></g></svg>
          www.velmordesign.example
        </li>
      </ul>
    </div>

    <div class="address-band">
      <div class="address-band__dark">2715 N Parkline Road, Ste 348, McAllen, TX 78501</div>
      <div class="address-band__mark">VELMOR</div>
      <div class="address-band__grey"></div>
    </div>
  </section>

  <section class="card card--back">
    <div class="brand">
      <span class="brand__square"></span>
      <span class="brand__rule"></span>
      <p class="brand__name"><span>Velmor</span><span>Home</span><span>Design</span></p>
    </div>
  </section>
</body>
</html>
```